Fernvale Craft Works business card design- Fine Art sculpture business (Contract guaranteed)

This business card is for a fine art business. Though we don't have a website up and running yet it should be up soon. I would like the business card to be elegant and fairly simple with a picture of one of my sculptures on the front (you might need to photoshop out the background) as well as my basic contact info (my name,phone # and e-mail). On the back I'd like it to be pretty simple with just "Notes" and some blank lines for writing in info.

Target Market(s)

High end artwork buyers

Industry/Entity Type

Art Gallery

Contact Information for Business Card

Marlo Prewitt Phone: (555) 213-4098 E-mail: marlo@quillbrookmail.com Facebook: @fernvalecraftworks Instagram: fernvalecraftworks

Colors

Designer to choose colors to be used in the design.

Requirements
Must have
• *A picture of one of my sculptures*, my name, business name (Fernvale Craft Works), e-mail, phone #, and a notes section on the back.
• Fernvale Craft Works
• Marlo Prewitt
• (555)213-4098
• marlo@quillbrookmail.com
• Facebook: @fernvalecraftworks
• Instagram: fernvalecraftworks
Nice to have
• It'd be nice if you can crop out the background in the sculpture pictures, which ever one you end up using.

```html
<!DOCTYPE html>
<html lang="en">
<head>
<meta charset="utf-8">
<title>Marlo Prewitt – Business Card</title>
<link rel="stylesheet" href="https://fonts.googleapis.com/css2?family=Quicksand:wght@400;500&display=swap">
<style>
  :root {
    --page-dark: #23103f;
    --page-light: #3b4a9a;
    --card-front: #24113f;
    --glow: #4a6ad6;
    --stone-light: #5a4ac4;
    --stone-deep: #2c1f6e;
    --back-top: #3e4592;
    --back-bottom: #2a1750;
    --panel: rgba(70, 55, 120, 0.35);
    --rule: #b9a3dc;
    --text: #ffffff;
    --edge: #1c1c24;
  }
  * { margin: 0; padding: 0; box-sizing: border-box; }
  html, body { width: 1200px; height: 1200px; overflow: hidden; }
  body {
    position: relative;
    font-family: "Quicksand", sans-serif;
    color: var(--text);
    background: linear-gradient(200deg, var(--page-light) 0%, var(--page-dark) 60%, var(--page-light) 100%);
  }
  .card { position: absolute; overflow: hidden; }

  .card-front {
    left: 154px; top: 0; width: 956px; height: 600px;
    background: var(--card-front);
    border: 2px solid var(--edge);
    border-top: none;
  }
  .glow {
    position: absolute; left: 194px; top: 52px;
    width: 568px; height: 504px;
    clip-path: polygon(50% 0, 100% 50%, 50% 100%, 0 50%);
    background: radial-gradient(closest-side, var(--glow) 0%, rgba(74,106,214,0.6) 35%, rgba(36,17,63,0) 100%);
  }
  .sculpture {
    position: absolute; left: 392px; top: 76px; width: 178px; height: 380px;
    border-radius: 40% 40% 30% 30% / 20% 20% 10% 10%;
    background: linear-gradient(170deg, var(--stone-light) 0%, var(--stone-deep) 100%);
  }
  .brand {
    position: absolute; left: 40px; top: 46px; width: 110px;
    font-size: 16px; font-weight: 400; line-height: 1.2;
  }
  .owner-name {
    position: absolute; right: 38px; top: 28px;
    font-size: 46px; font-weight: 400; letter-spacing: 0.5px;
  }
  .contact {
    position: absolute; left: 40px; top: 490px;
    display: flex; align-items: center; gap: 14px;
  }
  .contact-icon { width: 43px; height: 66px; }
  .contact-lines { display: flex; flex-direction: column; gap: 16px; font-size: 24px; line-height: 1; }

  .card-back {
    left: 158px; top: 602px; width: 951px; height: 598px;
    background: linear-gradient(160deg, var(--back-top) 0%, var(--back-bottom) 100%);
    border-left: 2px solid var(--edge);
  }
  .notes-title {
    position: absolute; top: 88px; left: 0; right: 0;
    text-align: center; font-size: 42px; font-weight: 500;
  }
  .notes-panel {
    position: absolute; left: 106px; top: 150px; width: 738px; height: 354px;
    background: var(--panel); border-radius: 16px;
  }
  .note-line {
    position: absolute; left: 38px; width: 664px; height: 2px; background: var(--rule);
  }
</style>
</head>
<body>
  <section class="card card-front">
    <div class="glow"></div>
    <div class="sculpture" role="img" aria-label="Photograph of an amethyst geode sculpture on a stone base"></div>
    <div class="brand">Fernvale Craft Works</div>
    <h1 class="owner-name">Marlo Prewitt</h1>
    <div class="contact">
      <svg class="contact-icon" viewBox="0 0 43 66" aria-hidden="true">
        <rect x="2" y="2" width="39" height="62" rx="4" fill="none" stroke="#fff" stroke-width="3"/>
        <line x1="15" y1="8" x2="28" y2="8" stroke="#fff" stroke-width="2"/>
        <rect x="2" y="54" width="39" height="10" fill="#fff"/>
        <circle cx="21.5" cy="59" r="2.5" fill="var(--card-front)"/>
        <rect x="12" y="26" width="19" height="14" fill="none" stroke="#fff" stroke-width="1.5"/>
        <path d="M12 26 L21.5 34 L31 26 M12 40 L19 33 M31 40 L24 33" fill="none" stroke="#fff" stroke-width="1.2"/>
      </svg>
      <div class="contact-lines">
        <span class="phone">(555) 213-4098</span>
        <span class="email">marlo@quillbrookmail.com</span>
      </div>
    </div>
  </section>

  <section class="card card-back">
    <h2 class="notes-title">Notes:</h2>
    <div class="notes-panel">
      <div class="note-line" style="top:82px"></div>
      <div class="note-line" style="top:126px"></div>
      <div class="note-line" style="top:169px"></div>
      <div class="note-line" style="top:211px"></div>
      <div class="note-line" style="top:254px"></div>
      <div class="note-line" style="top:297px"></div>
    </div>
  </section>
</body>
</html>
```